Business card design incorporating discount offer

We are a trade services company and we need a double sided business card that is going to be used by our tradesmen to give to customers on completion of their jobs.

Below are the key elements of the card that we would like to include:

-Main logo with text 'Corvane Building Aid' underneath.
-Up to 12 smaller icon logos with text 'Your local all-trade experts' to emphasise the point that we cover all the trades
-Discount offer - 10% discount
-Telephone number and website address
-Blank space for tradesman to enter his/her name
-Request for customer feedback with feedback url

This business card will be printed on regular card. In the past we have favoured designs that use a black background but we're open to new ideas.

I have attached a few files:

-A simple wire frame example to show how this card could look with the different elements mentioned above, feel free to use a layout similar to this or come up with something totally different (biz-card.pdf)
-Front and back of a loyalty card the we've used in the past (this card was printed on plastic)
-Front and back of a key fob design that we've previously used (this card was printed on plastic)
-A logo file with the 12 small icons and the main logo image

If you need further images or information please ask.

```html
<!DOCTYPE html>
<html lang="en">
<head>
<meta charset="utf-8">
<title>Corvane Building Aid – Business Card</title>
<link rel="stylesheet" href="https://fonts.googleapis.com/css2?family=PT+Sans:wght@400;700&display=swap">
<style>
  :root {
    --page: #d0d1d3;
    --ink-dark: #1c1c1d;
    --ink-dark-2: #2c2c2e;
    --brand-blue: #1a78b8;
    --brand-blue-light: #2a8fd0;
    --accent-blue: #3aa0e0;
    --white: #ffffff;
    --plumbing: #2f9be0;
    --heating: #2b8fd6;
    --electrical: #8d9196;
    --handyman: #f2c21b;
    --multi: #2a86cc;
    --drainage: #7e8489;
    --kitchens: #27b3b0;
    --bathrooms: #b2338f;
    --pest: #6dbb3a;
    --carpentry: #f0a81e;
    --decorating: #e2403c;
    --building: #b88550;
  }
  * { box-sizing: border-box; margin: 0; padding: 0; }
  html, body {
    width: 883px; height: 1200px; overflow: hidden;
    background: var(--page);
    font-family: "PT Sans", Arial, sans-serif;
    color: var(--white);
  }
  .sheet { position: relative; width: 883px; height: 1200px; }
  .card {
    position: absolute; left: 130px;
    width: 622px; height: 349px; overflow: hidden;
    box-shadow: 0 2px 6px rgba(0,0,0,.25);
  }
  .card--front { top: 237px; }
  .card--back { top: 614px; }
  .face {
    position: absolute; left: 136.5px; top: -136.5px;
    width: 349px; height: 622px;
    transform: rotate(-90deg);
    display: flex; flex-direction: column;
  }
  .dark {
    background: linear-gradient(160deg, var(--ink-dark-2), var(--ink-dark) 60%, #101011);
  }
  .blue { background: var(--brand-blue); }

  /* front */
  .front-main { height: 405px; padding: 34px 30px 0; }
  .brand { display: flex; align-items: center; gap: 14px; }
  .brand__dot { width: 40px; height: 40px; border-radius: 50%; background: var(--accent-blue); }
  .brand__name { font-size: 56px; font-weight: 700; line-height: 1; }
  .tagline { margin-top: 26px; font-size: 29px; font-weight: 700; }
  .contact { margin-top: 72px; display: flex; align-items: center; gap: 14px; }
  .contact__icon { width: 44px; height: 44px; flex: none; }
  .contact__lines { font-size: 27px; line-height: 1.05; }
  .offer { height: 217px; padding: 26px 20px 0 30px; }
  .offer__value { font-size: 104px; font-weight: 700; line-height: .95; letter-spacing: -2px; }
  .offer__line { font-size: 23px; font-weight: 700; margin-top: 10px; }
  .offer__small { font-size: 14.5px; font-weight: 700; margin-top: 4px; }

  /* back */
  .trades { height: 389px; padding: 22px 22px 0; background: var(--brand-blue-light); }
  .trades__title { font-size: 25px; font-weight: 700; }
  .trades__grid {
    margin-top: 22px;
    display: grid; grid-template-columns: repeat(3, 1fr); row-gap: 14px;
  }
  .trade { display: flex; flex-direction: column; align-items: flex-start; }
  .trade__icon {
    width: 42px; height: 42px; border-radius: 7px;
    display: flex; align-items: center; justify-content: center;
    box-shadow: 0 2px 3px rgba(0,0,0,.3);
  }
  .trade__icon svg { width: 26px; height: 26px; }
  .trade__label { font-size: 16px; margin-top: 6px; color: var(--ink-dark); }
  .feedback { height: 233px; padding: 22px 22px 0; }
  .feedback__label { font-size: 20px; color: var(--accent-blue); }
  .feedback__field { margin-top: 8px; width: 92%; height: 52px; background: var(--white); }
  .feedback__ask { margin-top: 30px; font-size: 23px; }
  .feedback__url { font-size: 16px; margin-top: 2px; }
</style>
</head>
<body>
<main class="sheet">

  <section class="card card--front" aria-label="Card front">
    <div class="face">
      <div class="front-main dark">
        <div class="brand">
          <span class="brand__dot"></span>
          <span class="brand__name">Corvane</span>
        </div>
        <p class="tagline">Corvane Building Aid</p>
        <div class="contact">
          <svg class="contact__icon" viewBox="0 0 24 24" aria-hidden="true">
            <path fill="#fff" d="M6.6 10.8c1.4 2.8 3.8 5.1 6.6 6.6l2.2-2.2c.3-.3.7-.4 1-.2 1.1.4 2.3.6 3.6.6.6 0 1 .4 1 1V20c0 .6-.4 1-1 1C10.6 21 3 13.4 3 4c0-.6.4-1 1-1h3.5c.6 0 1 .4 1 1 0 1.3.2 2.5.6 3.6.1.3 0 .7-.2 1z"/>
          </svg>
          <div class="contact__lines">
            <p>0800 000 4412</p>
            <p>corvane-aid.co.uk</p>
          </div>
        </div>
      </div>
      <div class="offer blue">
        <p class="offer__value">10%</p>
        <p class="offer__line">discount with this card</p>
        <p class="offer__small">check our web site for full offer details</p>
      </div>
    </div>
  </section>

  <section class="card card--back" aria-label="Card back">
    <div class="face">
      <div class="trades">
        <h2 class="trades__title">Your local all-trade experts</h2>
        <div class="trades__grid">
          <div class="trade"><span class="trade__icon" style="background:var(--plumbing)"><svg viewBox="0 0 24 24"><path fill="#fff" d="M12 3c3 4.5 6 7.5 6 11a6 6 0 0 1-12 0c0-3.5 3-6.5 6-11z"/></svg></span><span class="trade__label">Plumbing</span></div>
          <div class="trade"><span class="trade__icon" style="background:var(--heating)"><svg viewBox="0 0 24 24"><path fill="#fff" d="M12 2c1 4 5 6 5 11a5 5 0 0 1-10 0c0-3 2-4 2-7 1 1 2 2 2 4 1-2 1-5 1-8z"/></svg></span><span class="trade__label">Heating- Gas</span></div>
          <div class="trade"><span class="trade__icon" style="background:var(--electrical)"><svg viewBox="0 0 24 24"><path fill="#fff" d="M13 2 5 14h6l-2 8 8-12h-6z"/></svg></span><span class="trade__label">Electrical</span></div>
          <div class="trade"><span class="trade__icon" style="background:var(--handyman)"><svg viewBox="0 0 24 24"><circle cx="12" cy="12" r="6" fill="none" stroke="#fff" stroke-width="3"/><circle cx="12" cy="12" r="2" fill="#fff"/></svg></span><span class="trade__label">Handyman</span></div>
          <div class="trade"><span class="trade__icon" style="background:var(--multi)"><svg viewBox="0 0 24 24"><path fill="#fff" d="M12 3 3 11h3v9h12v-9h3z"/></svg></span><span class="trade__label">Multi trades</span></div>
          <div class="trade"><span class="trade__icon" style="background:var(--drainage)"><svg viewBox="0 0 24 24"><path fill="none" stroke="#fff" stroke-width="3" d="M6 4v8a6 6 0 0 0 12 0V4"/></svg></span><span class="trade__label">Drainage</span></div>
          <div class="trade"><span class="trade__icon" style="background:var(--kitchens)"><svg viewBox="0 0 24 24"><rect x="5" y="4" width="14" height="16" rx="1" fill="none" stroke="#fff" stroke-width="2.5"/><path stroke="#fff" stroke-width="2" d="M5 9h14"/></svg></span><span class="trade__label">Kitchens</span></div>
          <div class="trade"><span class="trade__icon" style="background:var(--bathrooms)"><svg viewBox="0 0 24 24"><path fill="#fff" d="M3 11h18v2a6 6 0 0 1-6 6H9a6 6 0 0 1-6-6z"/></svg></span><span class="trade__label">Bathrooms</span></div>
          <div class="trade"><span class="trade__icon" style="background:var(--pest)"><svg viewBox="0 0 24 24"><ellipse cx="12" cy="13" rx="4" ry="6" fill="#fff"/><path stroke="#fff" stroke-width="2" d="M4 9l4 2M20 9l-4 2M4 17l4-2M20 17l-4-2"/></svg></span><span class="trade__label">Pest control</span></div>
          <div class="trade"><span class="trade__icon" style="background:var(--carpentry)"><svg viewBox="0 0 24 24"><path fill="#fff" d="M4 18 16 4l4 4L8 20H4z"/></svg></span><span class="trade__label">Carpentry</span></div>
          <div class="trade"><span class="trade__icon" style="background:var(--decorating)"><svg viewBox="0 0 24 24"><rect x="5" y="3" width="14" height="8" rx="1" fill="#fff"/><path stroke="#fff" stroke-width="3" d="M12 11v10"/></svg></span><span class="trade__label">Decorating</span></div>
          <div class="trade"><span class="trade__icon" style="background:var(--building)"><svg viewBox="0 0 24 24"><path fill="#fff" d="M4 8h10V4h4v4h2v4H4zM10 12h4v9h-4z"/></svg></span><span class="trade__label">Building</span></div>
        </div>
      </div>
      <div class="feedback dark">
        <p class="feedback__label">Your Corvane tradesman:</p>
        <div class="feedback__field"></div>
        <p class="feedback__ask">Please leave feedback online</p>
        <p class="feedback__url">www.corvane-aid.co.uk/feedback</p>
      </div>
    </div>
  </section>

</main>
</body>
</html>
```